Flyer Design Project - Financial services business specialising in mortgages and insurance

I require a flyer to create interest in saving money with mortgages. We show people that they can save money on their mortgages by paying the mortgage of sooner. Therefore they no longer need to work for the bank, and that they can live their life debt free.
The call to action is that they pick up the phone and call me or make an inquiry online via our website.

We are a insurance and mortgage brokerage and the business name is called BRAVO. Website: www.bravolenders.co.nz (currently)
the new website that isn't quite live yet is viewable at
www.qortasites.com/bravo

Our tag line is Hearth Growth Tomorrow

The type of clients we are trying to engage with are home owners with existing mortgages.

Aged between 35-40, Professionals, Income bracket of $80k plus for the household, in a relationship, no more than two kids, live in our local area (West Auckland, New Zealand) they are driven to be successful and have a comfortable family life and be able to afford luxuries.(responsible)

We would like to see what options someone can come up other than the ususal. Needs to fit with our business name BRAVO + Tag line. As in we do things BRAVOER.

The flyer needs to show that we can help make a difference.

We will provide a free comparative market report on their house for an appointment and also if we cant save the prospect any money our guarantee is that we will give them a $20 voucher. (conditions will apply).

Ideally looking to have the flyer on a DLE size although we are open to options.

more than happy to discuss further if required to. I have attached my logo and my current image for home loans used on the website although i would like to see if there are any better options available than my current image.

Reason: Waiting on a couple of other designers who were sending there designs through before closing of.

Target Market(s)

home owners with an existing mortgage. Ages between 35-40, Professionals, Income 80k+

Industry/Entity Type

Insurance

Requirements
Must have
• A disclosure document is available upon request.
Our logo and contact details.
Call to action
Nice to have
• Want to focus on the lifestyles and goals rather than the actual payment of the mortgage.
Should not have
• We don't want to be saying the same boring message as most mortgage brokers are saying ie. Call us we can save you thousands of dollars.
We a need a reason for them to call us to go with our image and brand.

```html
<!DOCTYPE html>
<html lang="en">
<head>
<meta charset="utf-8">
<title>Bravo – Home Loan Flyer</title>
<link href="https://fonts.googleapis.com/css2?family=Ubuntu:wght@400;500;700&display=swap" rel="stylesheet">
<style>
  :root {
    --brand-blue: #1767b2;
    --pale-blue: #dcebf7;
    --ink: #111111;
    --tagline-grey: #4a4a4a;
    --backdrop: #e2e2e2;
    --white: #ffffff;
  }
  * { box-sizing: border-box; margin: 0; padding: 0; }
  html, body {
    width: 1200px;
    height: 900px;
    overflow: hidden;
    background: var(--backdrop);
    font-family: "Ubuntu", sans-serif;
  }
  .flyer {
    position: absolute;
    left: 413px;
    top: 54px;
    width: 374px;
    height: 792px;
    background: var(--white);
    border: 1px solid #333;
    overflow: hidden;
  }
  .hero-image {
    position: absolute;
    left: 20px;
    top: 14px;
    width: 334px;
    height: 214px;
    background: linear-gradient(180deg, #f3f5f8 0%, #e3e9f0 55%, #f7f7f7 100%);
  }
  .brand-name {
    position: absolute;
    left: 0;
    right: 0;
    top: 212px;
    text-align: center;
    font-size: 72px;
    font-weight: 500;
    line-height: 1;
    color: var(--brand-blue);
    letter-spacing: 1px;
  }
  .tagline {
    position: absolute;
    right: 52px;
    top: 298px;
    font-size: 22px;
    font-weight: 400;
    color: var(--tagline-grey);
  }
  .headline-band {
    position: absolute;
    left: 0;
    top: 338px;
    width: 100%;
    height: 92px;
    background: var(--brand-blue);
    color: var(--white);
    text-align: center;
    padding-top: 5px;
  }
  .headline {
    font-size: 27px;
    font-weight: 700;
    line-height: 40px;
  }
  .headline .emphasis { font-size: 40px; }
  .services-panel {
    position: absolute;
    left: 0;
    top: 430px;
    width: 100%;
    height: 250px;
    background: var(--pale-blue);
    color: var(--ink);
    text-align: center;
    padding-top: 11px;
  }
  .intro {
    font-size: 13px;
    font-weight: 700;
    line-height: 18px;
    padding: 0 22px;
  }
  .services-title {
    margin-top: 10px;
    font-size: 13px;
    font-weight: 700;
    line-height: 18px;
  }
  .services-list {
    list-style: none;
    font-size: 13px;
    line-height: 18px;
  }
  .guarantees {
    margin-top: 8px;
    font-size: 12.5px;
    font-weight: 700;
    line-height: 17px;
    color: var(--brand-blue);
    padding: 0 18px;
  }
  .offer-band {
    position: absolute;
    left: 0;
    top: 680px;
    width: 100%;
    height: 112px;
    background: var(--brand-blue);
    color: var(--white);
    text-align: center;
    padding-top: 7px;
  }
  .offer { font-size: 18px; font-weight: 500; line-height: 24px; }
  .offer .figure { font-size: 25px; }
  .conditions { font-size: 11px; font-weight: 700; line-height: 13px; }
  .call-to-action { margin-top: 9px; font-size: 13px; font-weight: 700; line-height: 17px; }
  .website { font-size: 12px; font-weight: 500; line-height: 16px; }
  .disclosure { font-size: 10px; font-weight: 400; line-height: 13px; }
</style>
</head>
<body>
  <article class="flyer">
    <div class="hero-image" role="img" aria-label="Photo of a smiling family of four leaning together beneath a pale house roof outline"></div>
    <div class="brand-name">BRAVO</div>
    <div class="tagline">Hearth Growth Tomorrow</div>

    <section class="headline-band">
      <h1 class="headline">We will find you the<br>right <span class="emphasis">home</span> loan!</h1>
    </section>

    <section class="services-panel">
      <p class="intro">BRAVO is able to assist you with sourcing a mortgage that suits your budget on your behalf saving you time and money.</p>
      <p class="services-title">Our services include</p>
      <ul class="services-list">
        <li>• Financing your new home</li>
        <li>• Pre-approval of home loans</li>
        <li>• Financing for investment properties</li>
        <li>• Re-financing and restructuring</li>
        <li>• Business &amp; Commercial Loans</li>
      </ul>
      <p class="guarantees">Free market report on your home at every appointment<br>Can't save you money? Get a $20 voucher*</p>
    </section>

    <section class="offer-band">
      <p class="offer">Loans up to <span class="figure">95%</span> are available</p>
      <p class="conditions">(credit criteria and *conditions apply)</p>
      <p class="call-to-action">Call us today 09 555 0142 or 021 555 0187</p>
      <p class="website">www.bravolenders.co.nz</p>
      <p class="disclosure">A disclosure document is available upon request.</p>
    </section>
  </article>
</body>
</html>
```